Fentra bottle Label (Yoghurt drink)

Label for a 300 ml yoghurt drink bottle in 3 flavours.

General description:
• This is to design a sleeve shrink label for a Yoghurt Drink bottle in three flavours, Classic, Strawberry and Blueberry.
• Attached 3 photos: The one with FENTRA brand in the current design we want to replace using the same bottle.
• Graphically, the design is to be similar to the examples provided for draveno and glimwave.
• Use font and barcode size to be readable and legal.
• Minimize the use of the upper third of the bottle as it will be distorted when the label shrinks to the bottle.
• Professional and experienced designers only are welcome, please do not waste your time otherwise.

Bottle dimensions:
• Base across: 61 mm
• Height: 145 mm (approximate)

Graphical description:
• White colour with bands at the top and bottom similar to the one in “draveno” example provided (not necessarily identical, feel free to be creative.
• The upper and lower bands to be: Green for “classic”, Pink or red for strawberry and purple for blueberry flavour.
• On the front: the brand name “Fentra” and description “Yoghurt Drink” to be graphically attractive.
• On the front: two or more pieces of strawberry or blueberry for each flavour placed nicely with the option to include “yoghurt splash” or any suitable affects you deem suitable.
• For the Classic flavour, use the words (Classic, Lassi, Ayran) in the same location for the berries done in a graphically suitable manner.
• Colour temperature for the three flavours to be similar.

Information and objects on the label:
Front:
• The word “Fentra” (brand name)
• “Yoghurt drink” (Product description)
• “300 ml” (size)
• Picture of Strawberries for strawberry flavour.
• Picture of Blueberries for blueberry flavour.
• The words (Classic, Lassi, Ayran) in the place used for the strawberries in the flavoured type, distributed to look graphically suitable for the overall design.

Back:
• Ingredient: Milk/milk solids, culture, salt, water, sugar, colour, flavour. (this is to be finalized later)
• Nutrition information table: (to be provided later).
• Barcode (to be provided later)
• Product of Australia
• Helmin Corvase Pty Ltd, 7/4 Pellow Rd, Malaga, WA 6090
• info@fentra-example.com.au 0491862375
• Keep under 5⁰ C
• Best before date printed on the bottle
• Shake well (to be located on the side at the top)
• Recycle icon.

Health benefits: (to be located suitably, possibly on the side with vertical orientation)
• Rich in probiotic bacteria and vitamins.
• Improves digestion and bowel motion.
• Supports weight control and fat loss.

Target Market(s)

General consumers

Industry/Entity Type

Grocery Store

Font styles to use
Sans Serif

Colors
abd037
b768aa
f04a50

Requirements
Must have
• The details in the project description
• The design must be simple and neat.
• Please use the shape of the current bottle "Fentra" as in the attached photo.
Should not have
• Busy, cluttered, or empty and incomplete designs.

```html
<!DOCTYPE html>
<html lang="en">
<head>
<meta charset="utf-8">
<title>Fentra Yoghurt Drink Labels</title>
<link rel="stylesheet" href="https://fonts.googleapis.com/css2?family=Roboto+Condensed:wght@300;400;700&display=swap">
<style>
  :root {
    --canvas: #ffffff;
    --label-white: #ffffff;
    --cream: #ece9e1;
    --ink: #1a1a1a;
    --brand-green: #abd037;
    --strawberry: #c11f2d;
    --strawberry-tint: #ee6b75;
    --classic: #a7cc34;
    --classic-tint: #cde86c;
    --blueberry: #2e5d96;
    --blueberry-tint: #7f9fcb;
  }
  html, body {
    margin: 0;
    padding: 0;
    width: 1200px;
    height: 1200px;
    overflow: hidden;
    background: var(--canvas);
  }
  .range-sheet {
    display: block;
    width: 1200px;
    height: 1200px;
    font-family: "Roboto Condensed", Arial, sans-serif;
  }
  .bottle--strawberry { --tone: var(--strawberry); --tint: var(--strawberry-tint); }
  .bottle--classic { --tone: var(--classic); --tint: var(--classic-tint); }
  .bottle--blueberry { --tone: var(--blueberry); --tint: var(--blueberry-tint); }

  .bottle__cap, .bottle__shoulder, .bottle__base-band { fill: var(--tone); }
  .bottle__body { fill: var(--label-white); }
  .bottle__tint-band { fill: var(--tint); }
  .bottle__cream { fill: var(--cream); }
  .bottle__neck { fill: #e6e6e6; }
  .bottle__rule { fill: var(--label-white); }
  .bottle__outline { fill: none; stroke: #d8d8d8; stroke-width: 1.5; }

  .brand-dot { fill: var(--tone); }
  .brand-name { fill: var(--tone); font-weight: 700; font-size: 38px; letter-spacing: 1px; }
  .product-title { fill: var(--ink); font-weight: 700; font-size: 42px; }
  .product-subtitle { fill: var(--ink); font-weight: 300; font-size: 42px; }
  .flavour-name { fill: var(--label-white); font-weight: 700; font-size: 24px; letter-spacing: 1px; }
  .volume { fill: var(--label-white); font-weight: 400; font-size: 17px; }

  .range-brand__dot { fill: var(--brand-green); }
  .range-brand__name { fill: var(--brand-green); font-weight: 700; font-size: 72px; letter-spacing: 2px; }
</style>
</head>
<body>
<svg class="range-sheet" viewBox="0 0 1200 1200" xmlns="http://www.w3.org/2000/svg">
  <defs>
    <clipPath id="bottle-body">
      <path d="M85,120 L235,120 C235,180 312,220 312,320 L312,840 Q312,880 272,880 L48,880 Q8,880 8,840 L8,320 C8,220 85,180 85,120 Z"/>
    </clipPath>
    <linearGradient id="strawberry-fill" x1="0" y1="0" x2="0" y2="1">
      <stop offset="0" stop-color="#d4353a"/>
      <stop offset="0.7" stop-color="#a91c24"/>
      <stop offset="1" stop-color="#eeeae2"/>
    </linearGradient>
    <linearGradient id="blueberry-fill" x1="0" y1="0" x2="0" y2="1">
      <stop offset="0" stop-color="#5a76a8"/>
      <stop offset="0.7" stop-color="#3c5488"/>
      <stop offset="1" stop-color="#eeeae2"/>
    </linearGradient>
    <linearGradient id="splash-fill" x1="0" y1="0" x2="0" y2="1">
      <stop offset="0" stop-color="#ffffff"/>
      <stop offset="1" stop-color="#e4e1d8"/>
    </linearGradient>
  </defs>

  <!-- Range brand -->
  <g class="range-brand">
    <circle class="range-brand__dot" cx="318" cy="176" r="18"/>
    <text class="range-brand__name" x="348" y="202">FENTRA</text>
  </g>

  <!-- Strawberry -->
  <g class="bottle bottle--strawberry" transform="translate(90,248)">
    <rect class="bottle__cap" x="74" y="0" width="172" height="104" rx="10"/>
    <rect class="bottle__neck" x="80" y="104" width="160" height="16" rx="4"/>
    <g clip-path="url(#bottle-body)">
      <rect class="bottle__body" x="0" y="100" width="320" height="790"/>
      <path class="bottle__shoulder" d="M0,100 H320 V300 C250,330 150,250 0,300 Z"/>
      <rect role="img" aria-label="Strawberries with yoghurt splash" x="40" y="440" width="280" height="160" fill="url(#strawberry-fill)"/>
      <rect class="bottle__cream" x="0" y="600" width="320" height="120"/>
      <rect class="bottle__tint-band" x="0" y="675" width="320" height="24"/>
      <rect class="bottle__tint-band" x="0" y="712" width="320" height="30"/>
      <rect class="bottle__tint-band" x="0" y="752" width="320" height="28"/>
      <rect class="bottle__base-band" x="0" y="790" width="320" height="100"/>
      <rect class="bottle__rule" x="0" y="842" width="320" height="4"/>
    </g>
    <path class="bottle__outline" d="M85,120 L235,120 C235,180 312,220 312,320 L312,840 Q312,880 272,880 L48,880 Q8,880 8,840 L8,320 C8,220 85,180 85,120 Z"/>
    <circle class="brand-dot" cx="110" cy="384" r="9"/>
    <text class="brand-name" x="126" y="398">FENTRA</text>
    <text class="product-title" x="72" y="660">YOGHURT</text>
    <text class="product-subtitle" x="72" y="696">DRINK</text>
    <text class="flavour-name" x="66" y="812">STRAWBERRY</text>
    <text class="flavour-name" x="66" y="836">FLAVOUR</text>
    <text class="volume" x="66" y="866">300ml</text>
  </g>

  <!-- Classic -->
  <g class="bottle bottle--classic" transform="translate(440,248)">
    <rect class="bottle__cap" x="74" y="0" width="172" height="104" rx="10"/>
    <rect class="bottle__neck" x="80" y="104" width="160" height="16" rx="4"/>
    <g clip-path="url(#bottle-body)">
      <rect class="bottle__body" x="0" y="100" width="320" height="790"/>
      <path class="bottle__shoulder" d="M0,100 H320 V300 C250,330 150,250 0,300 Z"/>
      <rect role="img" aria-label="Yoghurt splash" x="0" y="440" width="320" height="160" fill="url(#splash-fill)"/>
      <rect class="bottle__cream" x="0" y="600" width="320" height="120"/>
      <rect class="bottle__tint-band" x="0" y="675" width="320" height="24"/>
      <rect class="bottle__tint-band" x="0" y="712" width="320" height="30"/>
      <rect class="bottle__tint-band" x="0" y="752" width="320" height="28"/>
      <rect class="bottle__base-band" x="0" y="790" width="320" height="100"/>
      <rect class="bottle__rule" x="0" y="842" width="320" height="4"/>
    </g>
    <path class="bottle__outline" d="M85,120 L235,120 C235,180 312,220 312,320 L312,840 Q312,880 272,880 L48,880 Q8,880 8,840 L8,320 C8,220 85,180 85,120 Z"/>
    <circle class="brand-dot" cx="110" cy="384" r="9"/>
    <text class="brand-name" x="126" y="398">FENTRA</text>
    <text class="product-title" x="72" y="660">YOGHURT</text>
    <text class="product-subtitle" x="72" y="696">DRINK</text>
    <text class="flavour-name" x="66" y="812">CLASSIC</text>
    <text class="flavour-name" x="66" y="836">LASSI, AYRAN</text>
    <text class="volume" x="66" y="866">300ml</text>
  </g>

  <!-- Blueberry -->
  <g class="bottle bottle--blueberry" transform="translate(790,248)">
    <rect class="bottle__cap" x="74" y="0" width="172" height="104" rx="10"/>
    <rect class="bottle__neck" x="80" y="104" width="160" height="16" rx="4"/>
    <g clip-path="url(#bottle-body)">
      <rect class="bottle__body" x="0" y="100" width="320" height="790"/>
      <path class="bottle__shoulder" d="M0,100 H320 V300 C250,330 150,250 0,300 Z"/>
      <rect role="img" aria-label="Blueberries with leaves and yoghurt splash" x="50" y="450" width="260" height="150" fill="url(#blueberry-fill)"/>
      <rect class="bottle__cream" x="0" y="600" width="320" height="120"/>
      <rect class="bottle__tint-band" x="0" y="675" width="320" height="24"/>
      <rect class="bottle__tint-band" x="0" y="712" width="320" height="30"/>
      <rect class="bottle__tint-band" x="0" y="752" width="320" height="28"/>
      <rect class="bottle__base-band" x="0" y="790" width="320" height="100"/>
      <rect class="bottle__rule" x="0" y="842" width="320" height="4"/>
    </g>
    <path class="bottle__outline" d="M85,120 L235,120 C235,180 312,220 312,320 L312,840 Q312,880 272,880 L48,880 Q8,880 8,840 L8,320 C8,220 85,180 85,120 Z"/>
    <circle class="brand-dot" cx="110" cy="384" r="9"/>
    <text class="brand-name" x="126" y="398">FENTRA</text>
    <text class="product-title" x="72" y="660">YOGHURT</text>
    <text class="product-subtitle" x="72" y="696">DRINK</text>
    <text class="flavour-name" x="66" y="812">BLUEBERRY</text>
    <text class="flavour-name" x="66" y="836">FLAVOUR</text>
    <text class="volume" x="66" y="866">300ml</text>
  </g>
</svg>
</body>
</html>
```